Quorvan Stationery Design Project

We need stationary design that goes with the attached logo. We have logo in two different versions. One in Red/Black and the other in Blue/Green. Red/Black is going to be our primary color and we are planning to use Blue/Green occasionally as necessary.

So we need stationary design in both color combinations. Maybe you can work with Red/Black first and once we decide on the design, then you can show the Blue/Green variation.

Please see the attached png and psd files for logo.

Target Market(s)

IT departments of Medium size Enterprises.

Industry/Entity Type

Work

Requirements
Must have
• -Letter head
-Cover page design for white papers and articles that are going to publish
-Business Card
-Envelope design
Nice to have
• - High level design template that we can follow for our internal web applications

```html
<!DOCTYPE html>
<html lang="en">
<head>
<meta charset="utf-8">
<title>Quorvan Stationery</title>
<link rel="stylesheet" href="https://fonts.googleapis.com/css2?family=Tinos:wght@400;700&family=PT+Sans+Narrow:wght@400;700&family=Lobster&display=swap">
<style>
  :root {
    --ink: #000000;
    --red: #e0161b;
    --panel: #bdbdbd;
    --paper: #ffffff;
    --title-font: "Tinos", "Times New Roman", serif;
    --body-font: "PT Sans Narrow", "Arial Narrow", sans-serif;
  }
  html, body { margin: 0; padding: 0; overflow: hidden; }
  body { width: 1200px; height: 1000px; background: var(--paper); position: relative; font-family: var(--body-font); }
  .shapes { position: absolute; left: 0; top: 0; }
  .abs { position: absolute; margin: 0; white-space: nowrap; }
  .section-title { font-family: var(--title-font); font-weight: 700; color: var(--ink); line-height: 1; text-align: center; }
  .brand { display: flex; align-items: center; gap: 8px; }
  .brand-mark { background: var(--red); display: block; }
  .brand-name { font-family: var(--body-font); font-weight: 700; color: var(--ink); letter-spacing: 0.12em; line-height: 1; }
  .on-dark { color: var(--paper); font-weight: 700; }
  .web { color: var(--red); font-weight: 700; }
  .letter-body { font-weight: 700; font-size: 15px; line-height: 20px; color: var(--ink); }
  .signature-name { font-family: var(--title-font); font-size: 34px; text-decoration: underline; text-decoration-thickness: 2px; text-underline-offset: 6px; }
  .signature-role { font-family: var(--title-font); font-size: 22px; }
  .slogan { font-family: "Lobster", cursive; font-size: 25px; color: var(--ink); }
  .contact-line { display: flex; align-items: center; gap: 6px; }
  .contact-icon { width: 14px; height: 14px; border-radius: 50%; background: #556b2f; display: inline-block; }
</style>
</head>
<body>

<svg class="shapes" width="1200" height="1000" viewBox="0 0 1200 1000" aria-hidden="true">
  <defs>
    <clipPath id="cover-clip"><rect x="277" y="420" width="326" height="446"/></clipPath>
  </defs>
  <!-- envelope front -->
  <rect x="156" y="100" width="354" height="245" fill="var(--panel)"/>
  <rect x="171" y="113" width="329" height="225" fill="var(--paper)"/>
  <polygon points="171,300 500,160 500,338 171,338" fill="var(--ink)"/>
  <!-- business card panel -->
  <rect x="0" y="397" width="242" height="523" fill="var(--panel)"/>
  <rect x="32" y="493" width="198" height="135" fill="var(--paper)"/>
  <polygon points="32,600 230,522 230,628 32,628" fill="var(--ink)"/>
  <rect x="27" y="705" width="200" height="163" fill="var(--paper)"/>
  <!-- cover -->
  <rect x="263" y="390" width="347" height="485" fill="var(--panel)"/>
  <rect x="277" y="420" width="326" height="446" fill="var(--paper)"/>
  <g clip-path="url(#cover-clip)" stroke-width="12" fill="none">
    <line x1="392" y1="410" x2="262" y2="600" stroke="var(--ink)"/>
    <line x1="425" y1="410" x2="262" y2="648" stroke="var(--red)"/>
    <line x1="462" y1="410" x2="262" y2="702" stroke="var(--ink)"/>
    <line x1="615" y1="590" x2="425" y2="876" stroke="var(--ink)"/>
    <line x1="615" y1="668" x2="475" y2="876" stroke="var(--red)"/>
    <line x1="615" y1="730" x2="512" y2="876" stroke="var(--ink)"/>
  </g>
  <rect x="528" y="420" width="12" height="298" fill="var(--ink)"/>
  <rect x="350" y="604" width="12" height="262" fill="var(--ink)"/>
  <!-- letterhead -->
  <rect x="625" y="58" width="575" height="942" fill="var(--panel)"/>
  <rect x="650" y="72" width="545" height="918" fill="var(--paper)"/>
  <polygon points="650,842 1195,945 1195,990 650,990" fill="var(--ink)"/>
</svg>

<!-- envelope front -->
<h2 class="abs section-title" style="left:200px;top:70px;width:230px;font-size:27px;">envelope front</h2>
<div class="abs brand" style="left:180px;top:146px;"><span class="brand-mark" style="width:14px;height:14px;"></span><span class="brand-name" style="font-size:22px;">QUORVAN</span></div>
<p class="abs on-dark" style="left:183px;top:300px;font-size:15px;line-height:19px;">123, street name, city/state<br>country postal code</p>
<p class="abs web" style="left:438px;top:323px;font-size:8px;">www.company.com</p>

<!-- business card -->
<h2 class="abs section-title" style="left:0;top:403px;width:242px;font-size:38px;line-height:40px;">business card<br>front</h2>
<div class="abs brand" style="left:38px;top:508px;"><span class="brand-mark" style="width:11px;height:11px;"></span><span class="brand-name" style="font-size:16px;">QUORVAN</span></div>
<p class="abs on-dark" style="left:135px;top:565px;font-size:10px;line-height:13px;">123, street, city/state<br>country, postal code</p>
<p class="abs on-dark contact-line" style="left:134px;top:598px;font-size:6px;"><span class="contact-icon" style="width:7px;height:7px;"></span>123456</p>
<p class="abs on-dark contact-line" style="left:134px;top:613px;font-size:6px;"><span class="contact-icon" style="width:7px;height:7px;"></span>company@domain.com</p>
<p class="abs web" style="left:34px;top:617px;font-size:7px;">www.company.com</p>
<h2 class="abs section-title" style="left:0;top:655px;width:242px;font-size:40px;">back</h2>
<div class="abs brand" style="left:55px;top:733px;"><span class="brand-mark" style="width:14px;height:14px;"></span><span class="brand-name" style="font-size:22px;">QUORVAN</span></div>
<p class="abs slogan" style="left:27px;top:796px;width:200px;text-align:center;">here is slogan</p>

<!-- cover -->
<h2 class="abs section-title" style="left:263px;top:372px;width:347px;font-size:46px;">cover</h2>
<div class="abs brand" style="left:370px;top:648px;"><span class="brand-mark" style="width:16px;height:16px;"></span><span class="brand-name" style="font-size:30px;">QUORVAN</span></div>

<!-- letterhead -->
<h1 class="abs section-title" style="left:625px;top:-6px;width:575px;font-size:74px;">letterhead</h1>
<div class="abs brand" style="left:662px;top:128px;"><span class="brand-mark" style="width:24px;height:24px;"></span><span class="brand-name" style="font-size:38px;">QUORVAN</span></div>
<div class="abs letter-body" style="left:659px;top:295px;">
  <p style="margin:0 0 24px;">dear client,</p>
  <p style="margin:0 0 24px;">akjhjkasgigeyghdbfmxncbxvcbvfjhsjkgfaweuagriuafjksdbfadsvfhjdflsdjkfk<br>sjfhgdfiegfbjsbvnm,cbvnjfvhjsdfkajskbfdkjv ncv sdfbs,x vmn nvzdfj,s</p>
  <p style="margin:0;">jhgskfvdgcvsdbmvsaemwvjsdbv,sfjrhfjnv xcv bsfhejfbka.bff,bxfjbhsaf,b,<br>bfmnbsdfmmevjhfnsm,bmvx vn,f,b kvdjv sk jbskj jkbjka kj</p>
</div>
<p class="abs signature-name" style="left:1057px;top:762px;">name</p>
<p class="abs signature-role" style="left:1060px;top:808px;">position</p>
<p class="abs on-dark" style="left:652px;top:873px;font-size:17px;line-height:23px;">123, street, city/state<br>cauntry, postal code</p>
<p class="abs on-dark contact-line" style="left:658px;top:933px;font-size:12px;"><span class="contact-icon"></span>123456</p>
<p class="abs on-dark contact-line" style="left:658px;top:960px;font-size:12px;"><span class="contact-icon"></span>company@domain.com</p>
<p class="abs web" style="left:1068px;top:962px;font-size:13px;">www.company.com</p>

</body>
</html>
```